Tamkor, a service provider dedicated to improving the performance of a website

Tamkor offers optimization and performance improvement for all types of websites (showcase sites, e-commerce, ...), with the aim of improving their ranking on Vintrel and their customer transformation rate. The main benefits consist in optimizing the factors of a site. In addition, we also offer content creation (description of product sheets, services, ...), Vintrel Ads campaign management, migration version for Prestashop / Wordpress, etc. The design must be a fresh image, dynamic, why not "fun", but also serious. No favorite color, carte blanche on this point;)

```html
<!DOCTYPE html>
<html lang="en">
<head>
<meta charset="utf-8">
<title>Tamkor – Business Card</title>
<link rel="stylesheet" href="https://fonts.googleapis.com/css2?family=Lato:wght@400;700;900&display=swap">
<style>
  :root {
    --backdrop: #2a2a2a;
    --card-light: #ececec;
    --brand-blue: #3a4fa3;
    --card-blue: #1f4a8c;
    --ink: #2e2e2e;
    --rule: #9a9a9a;
    --white: #ffffff;
  }
  * { margin: 0; padding: 0; box-sizing: border-box; }
  html, body {
    width: 1200px;
    height: 1200px;
    overflow: hidden;
    background: var(--backdrop);
    font-family: "Lato", sans-serif;
  }
  .canvas { position: relative; width: 1200px; height: 1200px; }
  .card {
    position: absolute;
    top: 310px;
    height: 594px;
  }
  .card-front {
    left: 234px;
    width: 364px;
    background: var(--card-light);
    color: var(--ink);
    text-align: center;
  }
  .card-back {
    left: 627px;
    width: 369px;
    background: var(--card-blue);
    display: flex;
    align-items: center;
    justify-content: center;
  }
  .wordmark {
    position: absolute;
    top: 118px;
    left: 0;
    width: 100%;
    font-weight: 900;
    font-size: 84px;
    letter-spacing: -1px;
    color: var(--brand-blue);
    line-height: 1;
  }
  .person-name {
    position: absolute;
    top: 336px;
    width: 100%;
    font-size: 22px;
    font-weight: 400;
    color: var(--brand-blue);
    letter-spacing: 0.3px;
  }
  .person-role {
    position: absolute;
    top: 360px;
    width: 100%;
    font-size: 17px;
  }
  .contact-divider {
    position: absolute;
    top: 400px;
    left: 0;
    width: 100%;
  }
  .contact-lines {
    position: absolute;
    top: 427px;
    width: 100%;
    font-size: 17px;
    line-height: 22px;
  }
  .address-rule {
    position: absolute;
    top: 504px;
    left: 91px;
    width: 187px;
    height: 1px;
    background: var(--rule);
  }
  .address-lines {
    position: absolute;
    top: 513px;
    width: 100%;
    font-size: 17px;
    line-height: 22px;
  }
  .back-name {
    font-weight: 900;
    font-size: 72px;
    color: var(--white);
    letter-spacing: -1px;
  }
</style>
</head>
<body>
<main class="canvas">
  <section class="card card-front">
    <div class="wordmark">Tamkor</div>
    <div class="person-name">MAREK OLSEN</div>
    <div class="person-role">Managing Director</div>
    <svg class="contact-divider" width="364" height="22" viewBox="0 0 364 22" aria-hidden="true">
      <line x1="91" y1="11" x2="146" y2="11" stroke="#9a9a9a" stroke-width="1"/>
      <line x1="218" y1="11" x2="278" y2="11" stroke="#9a9a9a" stroke-width="1"/>
      <g fill="#3a4fa3">
        <circle cx="159" cy="11" r="10"/>
        <circle cx="182" cy="11" r="10"/>
        <circle cx="204" cy="11" r="10"/>
      </g>
      <path d="M155 6 q-1 6 6 10 l2-2 -2.5-2 -1.5 1 q-2-1.5-2.5-3.5 l1.2-1.2 -1.5-2.8z" fill="#fff"/>
      <rect x="176.5" y="7" width="11" height="8" rx="1" fill="#fff"/>
      <path d="M176.5 7.5 l5.5 4 5.5-4" fill="none" stroke="#3a4fa3" stroke-width="1"/>
      <circle cx="204" cy="11" r="5.5" fill="none" stroke="#fff" stroke-width="1.4"/>
      <path d="M198.5 11 h11 M204 5.5 q-3 5.5 0 11 M204 5.5 q3 5.5 0 11" fill="none" stroke="#fff" stroke-width="1"/>
    </svg>
    <div class="contact-lines">
      <p>312 408 7150</p>
      <p>hello@tamkorweb.com</p>
      <p>www.tamkorweb.com</p>
    </div>
    <div class="address-rule"></div>
    <div class="address-lines">
      <p>87, Lindenweg Street,</p>
      <p>Norvale, 30418</p>
    </div>
  </section>
  <section class="card card-back">
    <div class="back-name">Tamkor</div>
  </section>
</main>
</body>
</html>
```